Creating a Label for the Wine "Cala Brisena"

Cala Brisena
Cala Brisena means “lost mountain. Cala Brisena is a mountain far away from everything, lost in a wild place. The dimensios shoul be between 9cm x 11,5 cm and 12cm x 8 cm.

```html
<!DOCTYPE html>
<html lang="en">
<head>
<meta charset="utf-8">
<title>Cala Brisena — Wine Label</title>
<link rel="stylesheet" href="https://fonts.googleapis.com/css2?family=Fira+Sans+Extra+Condensed:wght@300&family=Sacramento&display=swap">
<style>
  :root {
    --teal: #40c0cf;
    --teal-light: #e8f8fa;
    --mountain: #3d6fb0;
    --ink: #ffffff;
  }
  html, body {
    margin: 0;
    padding: 0;
    overflow: hidden;
    background: #ffffff;
  }
  .label {
    position: relative;
    width: 939px;
    height: 1200px;
    overflow: hidden;
    background:
      radial-gradient(circle at 100% 0%, #ffffff 0%, var(--teal-light) 8%, rgba(64,192,207,0) 62%),
      var(--teal);
    font-family: "Fira Sans Extra Condensed", sans-serif;
  }
  .mountains {
    position: absolute;
    inset: 0;
  }
  .mountain {
    fill: var(--mountain);
    opacity: 0.6;
  }
  .wine-name {
    position: absolute;
    left: 455px;
    top: 575px;
    margin: 0;
    transform: translate(-50%, -50%) rotate(-55deg);
    color: var(--ink);
    font-family: "Sacramento", cursive;
    font-weight: 400;
    font-size: 300px;
    line-height: 0.75;
    white-space: nowrap;
  }
  .wine-name .line {
    display: block;
  }
  .wine-name .line-first {
    padding-right: 260px;
  }
  .wine-name .line-second {
    padding-left: 120px;
  }
  .details {
    position: absolute;
    left: 500px;
    top: 1100px;
    width: 385px;
    height: 86px;
    display: flex;
    align-items: center;
    justify-content: space-between;
    color: var(--ink);
    font-weight: 300;
    font-size: 58px;
    line-height: 1;
  }
  .details .volume,
  .details .strength {
    white-space: nowrap;
  }
  .bird-mark {
    width: 62px;
    height: 76px;
  }
</style>
</head>
<body>
  <main class="label">
    <svg class="mountains" viewBox="0 0 939 1200" aria-hidden="true">
      <polygon class="mountain" points="618,653 939,1033 939,1200 132,1200"/>
      <polygon class="mountain" points="802,777 939,936 939,1200 442,1200"/>
    </svg>

    <h1 class="wine-name">
      <span class="line line-first">Cala</span>
      <span class="line line-second">Brisena</span>
    </h1>

    <div class="details">
      <span class="volume">0,75 lt</span>
      <svg class="bird-mark" viewBox="0 0 62 76" role="img" aria-label="Small bird illustration">
        <ellipse cx="31" cy="40" rx="26" ry="26" fill="#ffffff"/>
      </svg>
      <span class="strength">13% Alc.</span>
    </div>
  </main>
</body>
</html>
```